VORALUX SYSTEMS BUSINESS CARD DESIGN

WE WANT COMPLETE NEW DESIGN OF OUR BUSINESS CARD. WE ARE AN INTEGRATION COMPANY, WHERE WE INTEGRATE IOT/SMART SYSTEMS TO HOMES AND CORPORATE CUSTOMERS. WE SUPPLY AND INSTALL AUTOMATION PRODUCTS. THE FINAL DESIGN SHOULD COMMUNICATE TECHNOLOGY. THE CARD DESIGN SHOULD BE VERY IMPACT FULL. LOGO NEEDS TO BE THERE. IT WOULD NICE IF THE DESIGN WAS CLEAN. COLORS IS UP TO DESIGNER TO PLAY WITH, OR CAN STICK TO CORPORATE COLORS (FOLLOW LOGO). I HAVE ADDED FEW REFERENCE PHOTOS TO DRAW INSPIRATION MAYBE. I HAVE ADDED A HEX DESIGN, ITS NOT NECESSARY TO USE THIS DESIGN, ITS UPTO DESIGNER, JUST ADDED IF NEEDED TO PLAY WITH DESIGN.

Target Market(s)

Private end users and corporate clients

Industry/Entity Type

technology, home automation, home theaters, building management systems, IOT

Contact Information for Business Card

It should include Employee name, personal number, office number, email address, both in English and arabic. DETAILS TO INCLUDE :DANIEL MARUVEN, MOBILE 0097150738219,OFFCIE 009714368174, DANIEL@VORALUXSYS.CO

Requirements
Must have
• Should feel like a technology company from design. Details both and in English and arabic (or at least have provision for arabic in design).
Nice to have
• I would like logo on one side, and details on the other side. Logo design side should communicate technology with logo. Other side can be clean just with information or also have some design aspects following from logo side. it would be interesting to see submissions with square design as well (that looks like an app Icon). colors could be of logo, red black grey and white. I have added some designs to draw inspiration from

```html
<!DOCTYPE html>
<html lang="en">
<head>
<meta charset="utf-8">
<title>Voralux Systems – Business Card</title>
<link href="https://fonts.googleapis.com/css2?family=Open+Sans:wght@400;600;700&family=Michroma&display=swap" rel="stylesheet">
<style>
  :root {
    --backdrop: #1b1b1b;
    --card: #2a2a2b;
    --card-front: #262627;
    --silver: #c9c9cb;
    --white: #ffffff;
    --red: #e0202a;
    --trace: #4a4a4c;
    --trace-soft: #303031;
  }
  * { margin: 0; padding: 0; box-sizing: border-box; }
  html, body { width: 1200px; height: 800px; overflow: hidden; }
  body {
    background: var(--backdrop);
    font-family: "Open Sans", Arial, sans-serif;
    position: relative;
  }
  .card {
    position: absolute;
    top: 245px;
    width: 540px;
    height: 310px;
    overflow: hidden;
    box-shadow: 0 14px 30px rgba(0,0,0,.45);
  }
  .card--front { left: 40px; background: var(--card-front); }
  .card--back { left: 620px; background: var(--card); }

  .circuit-field {
    position: absolute;
    top: 0;
    height: 100%;
    width: 210px;
  }
  .card--front .circuit-field {
    left: 0;
    background: linear-gradient(90deg, var(--trace) 0%, var(--trace-soft) 70%, transparent 100%);
    opacity: .6;
  }
  .card--back .circuit-field {
    right: 0;
    width: 250px;
    background: linear-gradient(270deg, var(--trace) 0%, var(--trace-soft) 70%, transparent 100%);
    opacity: .6;
  }

  .brand { position: absolute; }
  .brand__name {
    display: flex;
    align-items: center;
    gap: 10px;
    font-weight: 700;
    white-space: nowrap;
  }
  .brand__mark { display: inline-block; background: var(--red); }
  .brand__division {
    font-family: "Michroma", "Open Sans", sans-serif;
    letter-spacing: .14em;
    white-space: nowrap;
  }

  .card--front .brand { left: 210px; top: 110px; }
  .card--front .brand__name { font-size: 30px; color: var(--silver); }
  .card--front .brand__mark { width: 18px; height: 18px; background: var(--silver); }
  .card--front .brand__division { margin-top: 14px; font-size: 10px; color: #8c8c8e; }

  .card--back .brand { left: 34px; top: 28px; }
  .card--back .brand__name { font-size: 24px; color: var(--white); }
  .card--back .brand__mark { width: 14px; height: 14px; }
  .card--back .brand__division { margin-top: 8px; font-size: 8px; color: var(--white); }

  .arabic-band {
    position: absolute;
    left: 34px;
    top: 102px;
    width: 230px;
    height: 30px;
    background: var(--white);
  }

  .contact { position: absolute; left: 40px; top: 146px; color: var(--white); }
  .contact__name { font-size: 17px; font-weight: 700; color: var(--red); letter-spacing: .01em; }
  .contact__role { font-size: 11px; margin-bottom: 8px; }
  .contact__address { font-size: 10.5px; line-height: 1.35; margin-bottom: 7px; }
  .contact__list { list-style: none; font-size: 10.5px; line-height: 1.45; }
  .contact__list li { display: flex; align-items: center; gap: 8px; }
  .contact__list svg { width: 10px; height: 10px; fill: var(--red); flex: none; }
</style>
</head>
<body>

  <section class="card card--front">
    <div class="circuit-field" role="img" aria-label="Faint circuit-trace pattern"></div>
    <div class="brand">
      <div class="brand__name"><span class="brand__mark"></span>VORALUX SYSTEMS</div>
      <div class="brand__division">A VORALUX GROUP DIVISION.</div>
    </div>
  </section>

  <section class="card card--back">
    <div class="circuit-field" role="img" aria-label="Faint circuit-trace pattern"></div>
    <div class="brand">
      <div class="brand__name"><span class="brand__mark"></span>VORALUX SYSTEMS</div>
      <div class="brand__division">A VORALUX GROUP DIVISION.</div>
    </div>
    <div class="arabic-band"></div>
    <div class="contact">
      <div class="contact__name">DANIEL MARUVEN</div>
      <div class="contact__role">President</div>
      <div class="contact__address">2214 Cedar Ridge Lane<br>Juneau, Alaska 45812</div>
      <ul class="contact__list">
        <li><svg viewBox="0 0 10 10"><path d="M2 0.5 L4 2.8 L3 4 Q4.5 6 6 7 L7.2 6 L9.5 8 L8 9.6 Q3 9 0.4 2 Z"/></svg>0097150738219</li>
        <li><svg viewBox="0 0 10 10"><path d="M2.5 0 H7.5 V10 H2.5 Z M3.3 1 V8 H6.7 V1 Z"/></svg>009714368174</li>
        <li><svg viewBox="0 0 10 10"><path d="M0 2 H10 V8 H0 Z M0.8 2.6 L5 5.6 L9.2 2.6 Z" fill-rule="evenodd"/></svg>daniel@voraluxsys.co</li>
        <li><svg viewBox="0 0 10 10"><circle cx="5" cy="5" r="4.5"/></svg>www.voraluxsys.co</li>
      </ul>
    </div>
  </section>

</body>
</html>
```